Copper Meadow Creamery Business cards

We need a logo design for our family dairy. Included on the cards should be my name/my husbands name/the dairy name/ all the phone numbers/address and email. The name is Copper Meadow Creamery, LLC. We would like to use our farm mascot pic on the card. We know the pictures I sent you are of a beef cow but she is the mascot of the farm. We were thinking that maybe put a picture of her head in the middle of the card with a "B" on one side and a "D" on the other side with a "C" around the picture of the cow. But we are open to any ideas. We are looking for something kind of professional and a design that that can be used on cards, clothing and a car sign. Black lettering and blue for the other color...or what looks good.

Target Market(s)

All

Industry/Entity Type

Farming

Contact Information for Business Card

Marla Dutton Owner (555)417-2093
Ronald Pfister Owner (555)238-7715
Copper Meadow Creamery, LLC (555)906-4182
Coppermeadowcreamery@mailbarn.test
7126 County Lane 91, Alderbrook, MN 50917

Font styles to use
Sans Serif

Colors
3176b5
3c7bb8
3277b5
0255a3

Requirements
Must have
• Some design that incorporates a drawing/pic of the cow pictures that were sent.
Nice to have
• no suggestions
Should not have
• no suggestions

```html
<!DOCTYPE html>
<html lang="en">
<head>
<meta charset="utf-8">
<title>Copper Meadow Creamery — Business Card</title>
<link href="https://fonts.googleapis.com/css2?family=Montserrat:wght@300;400;700&display=swap" rel="stylesheet">
<style>
  :root {
    --backdrop: #c7c0b6;
    --card: #ffffff;
    --brand-blue: #2a6fb5;
    --text-blue: #3c7bb8;
  }
  * { margin: 0; padding: 0; box-sizing: border-box; }
  html, body {
    width: 1200px;
    height: 848px;
    overflow: hidden;
    background: var(--backdrop);
    font-family: "Montserrat", Arial, sans-serif;
  }
  .business-card {
    position: absolute;
    left: 442px;
    top: 160px;
    width: 312px;
    height: 511px;
    background: var(--card);
    color: var(--text-blue);
    text-align: center;
  }
  .brand-mark {
    position: absolute;
    left: 96px;
    top: 25px;
    width: 120px;
    height: 120px;
  }
  .brand-name {
    position: absolute;
    left: 0;
    right: 0;
    top: 168px;
    font-size: 19px;
    font-weight: 700;
    color: var(--brand-blue);
  }
  .divider {
    position: absolute;
    left: 34px;
    width: 245px;
    top: 217px;
    height: 3px;
    background: var(--brand-blue);
  }
  .owner {
    position: absolute;
    left: 0;
    right: 0;
    font-size: 13.5px;
    line-height: 16px;
  }
  .owner--first { top: 246px; }
  .owner--second { top: 311px; }
  .owner__name { font-weight: 700; color: var(--brand-blue); }
  .owner__role, .owner__phone { font-weight: 300; }
  .company {
    position: absolute;
    left: 0;
    right: 0;
    top: 378px;
    font-size: 13.5px;
    line-height: 22px;
    font-weight: 300;
  }
  .company__name { font-weight: 700; color: var(--brand-blue); }
  .company__email { font-size: 12.5px; }
</style>
</head>
<body>
  <article class="business-card">
    <svg class="brand-mark" viewBox="0 0 120 120" aria-hidden="true">
      <circle cx="60" cy="60" r="55" fill="none" stroke="var(--brand-blue)" stroke-width="7"/>
    </svg>
    <h1 class="brand-name">Copper Meadow Creamery</h1>
    <div class="divider"></div>

    <section class="owner owner--first">
      <div class="owner__name">Marla Dutton</div>
      <div class="owner__role">Owner</div>
      <div class="owner__phone">(555)417-2093</div>
    </section>

    <section class="owner owner--second">
      <div class="owner__name">Ronald Pfister</div>
      <div class="owner__role">Owner</div>
      <div class="owner__phone">(555)238-7715</div>
    </section>

    <section class="company">
      <div class="company__name">Copper Meadow Creamery, LLC</div>
      <div class="company__phone">(555)906-4182</div>
      <div class="company__email">coppermeadowcreamery@mailbarn.test</div>
      <div class="company__street">7126 County Lane 91,</div>
      <div class="company__city">Alderbrook, MN 50917</div>
    </section>
  </article>
</body>
</html>
```